Turning Lecture Halls into Studios of Bold Discovery

This is for a book cover aimed at professors in higher education who want to infuse creative thinking into their classroom. It should have the title on the cover (see name of project). Our first idea is to have a stack of academic type books on a desk in black and white and then have a colorful rainbow light thread hitting the books. However, we are open to options! It has to be sophisticated, cool, and creative ;)

Target Market(s)

Higher Education Instructors

Industry/Entity Type

education

Font styles to use
Serif
Sans Serif

Requirements
Nice to have
• a creative feel of some sort
Should not have
• lightbulbs

```html
<!DOCTYPE html>
<html lang="en">
<head>
<meta charset="utf-8">
<title>Turning Lecture Halls into Studios of Bold Discovery – Book Cover</title>
<link rel="stylesheet" href="https://fonts.googleapis.com/css2?family=Yellowtail&family=Montserrat:wght@200;400;800&family=Nunito:wght@800;900&display=swap">
<style>
  :root {
    --page-bg: #ffffff;
    --ink-white: #ffffff;
    --accent-orange: #f7931e;
    --accent-blue: #29abe2;
    --accent-purple: #8b1a7e;
    --night: #1b1a1a;
    --smoke: #6d6c6a;
    --glow: #f4f4f2;
    --wood-dark: #3a2616;
    --wood-mid: #6b4a2e;
  }
  html, body {
    margin: 0;
    padding: 0;
    width: 1200px;
    height: 1200px;
    overflow: hidden;
    background: var(--page-bg);
  }
  .canvas {
    position: relative;
    width: 1200px;
    height: 1200px;
  }
  .book-cover {
    position: absolute;
    left: 220px;
    top: 30px;
    width: 760px;
    height: 1140px;
    overflow: hidden;
    background: var(--night);
  }
  .cover-art {
    position: absolute;
    inset: 0;
    width: 100%;
    height: 100%;
  }
  .cover-text {
    position: absolute;
    left: 0;
    width: 100%;
    margin: 0;
    text-align: center;
    line-height: 1;
    white-space: nowrap;
  }
  .title-script {
    font-family: "Yellowtail", cursive;
    font-weight: 400;
  }
  .title-lead {
    top: 100px;
    font-size: 68px;
    color: var(--accent-orange);
  }
  .title-light {
    top: 190px;
    font-family: "Montserrat", sans-serif;
    font-weight: 200;
    font-size: 108px;
    color: var(--ink-white);
    letter-spacing: 2px;
  }
  .title-bold {
    top: 300px;
    font-family: "Montserrat", sans-serif;
    font-weight: 800;
    font-size: 120px;
    color: var(--ink-white);
    letter-spacing: -2px;
  }
  .title-joiner {
    top: 418px;
    font-size: 54px;
    color: var(--ink-white);
  }
  .title-blue {
    font-family: "Nunito", sans-serif;
    font-weight: 900;
    font-size: 60px;
    color: var(--accent-blue);
    letter-spacing: -0.5px;
  }
  .title-blue.line-one { top: 482px; }
  .title-blue.line-two { top: 552px; }
  .subtitle {
    top: 645px;
    font-family: "Nunito", sans-serif;
    font-weight: 900;
    font-size: 25px;
    line-height: 31px;
    color: var(--accent-purple);
    letter-spacing: -0.3px;
  }
  .author-name {
    top: 1080px;
    font-family: "Montserrat", sans-serif;
    font-weight: 400;
    font-size: 36px;
    color: var(--ink-white);
    letter-spacing: 6px;
  }
</style>
</head>
<body>
<main class="canvas">
  <section class="book-cover">
    <svg class="cover-art" viewBox="0 0 760 1140" preserveAspectRatio="none" role="img" aria-label="Photograph of an open book on a wooden table, glowing white light and sparkles rising from its pages against a dark smoky backdrop">
      <defs>
        <linearGradient id="backdrop" x1="0" y1="0" x2="0" y2="1">
          <stop offset="0" stop-color="#1c1b1b"/>
          <stop offset="0.45" stop-color="#2a2928"/>
          <stop offset="0.8" stop-color="#4a4845"/>
          <stop offset="0.86" stop-color="#5b3f27"/>
          <stop offset="1" stop-color="#3a2616"/>
        </linearGradient>
        <radialGradient id="smoke" cx="0.5" cy="0.55" r="0.55">
          <stop offset="0" stop-color="#8a8986" stop-opacity="0.75"/>
          <stop offset="1" stop-color="#8a8986" stop-opacity="0"/>
        </radialGradient>
        <radialGradient id="light" cx="0.5" cy="0.78" r="0.35">
          <stop offset="0" stop-color="#ffffff"/>
          <stop offset="0.55" stop-color="#f4f4f2" stop-opacity="0.85"/>
          <stop offset="1" stop-color="#f4f4f2" stop-opacity="0"/>
        </radialGradient>
      </defs>
      <rect width="760" height="1140" fill="url(#backdrop)"/>
      <rect width="760" height="1140" fill="url(#smoke)"/>
      <rect width="760" height="1140" fill="url(#light)"/>
    </svg>

    <p class="cover-text title-script title-lead">Turning</p>
    <h1 class="cover-text title-light">LECTURE</h1>
    <p class="cover-text title-bold">HALLS</p>
    <p class="cover-text title-script title-joiner">into</p>
    <p class="cover-text title-blue line-one">STUDIOS OF</p>
    <p class="cover-text title-blue line-two">BOLD DISCOVERY</p>
    <p class="cover-text subtitle">CULTIVATING INNOVATION, INSPIRING MINDS,<br>AND TRANSFORMING EDUCATION<br>FOR A CREATIVE FUTURE</p>
    <p class="cover-text author-name">AUTHOR NAME</p>
  </section>
</main>
</body>
</html>
```